harborline slab pumping "just pump it"

I want very easy to understand cards that say everything we offer.
i want the company name/logo, phone number and email on the front of card.
i want the card to stand out, it can be red with black lettering.
on the back of the card i want it to list everything that we can do like a list
the motto is JUST PUMP IT.
the can be in the lower right corner of the back of the card

Target Market(s)

concrete contractors

Industry/Entity Type

Concrete

Contact Information for Business Card

back of the card
Owner:Marco Tellin
Phone:503)418-6093
Email: HSPumping@slabmail.example
address: 22816 se brindle ave Portland, OR 97236

Colors
ec1f27
000000
959595
5c5c5c
f04a50
ffffff
f37122

Requirements
Must have
• :we have years of experience in the world of concrete
• :our pumps can do up to 70 yards an hour
• :if you refer us to other contractors, will give you up to 10% off next pump job
• :don’t hesitate to call if you have any concrete related questions and to get a qoute
• Please put this on the front of the card, “just pump it” in the lower right corner

```html
<!DOCTYPE html>
<html lang="en">
<head>
<meta charset="utf-8">
<title>Harborline Slab Pumping – Business Cards</title>
<link href="https://fonts.googleapis.com/css2?family=Montserrat:wght@300;400;500;800&family=Roboto+Slab:wght@700&family=Roboto:wght@400&display=swap" rel="stylesheet">
<style>
  :root {
    --red: #ec1f27;
    --black: #000000;
    --white: #ffffff;
    --grey: #959595;
    --stage: #15150f;
  }
  * { margin: 0; padding: 0; box-sizing: border-box; }
  html, body {
    width: 1200px;
    height: 1200px;
    overflow: hidden;
    background: var(--stage);
  }
  .canvas { position: relative; width: 1200px; height: 1200px; }
  .card {
    position: absolute;
    left: 210px;
    width: 780px;
    height: 450px;
    border-radius: 40px;
    background: var(--black);
    overflow: hidden;
  }
  .card--front { top: 110px; }
  .card--back  { top: 640px; }
  .card__shapes { position: absolute; inset: 0; width: 780px; height: 450px; }

  .motto {
    position: absolute;
    right: 48px;
    font-family: "Montserrat", sans-serif;
    font-weight: 800;
    font-size: 30px;
    letter-spacing: 2px;
    line-height: 1;
  }

  /* front */
  .contact {
    position: absolute;
    top: 48px;
    right: 52px;
    text-align: right;
    color: var(--white);
  }
  .contact__name {
    font-family: "Roboto Slab", serif;
    font-weight: 700;
    font-size: 34px;
    color: var(--red);
    letter-spacing: 0.5px;
    line-height: 1;
  }
  .contact__role {
    font-family: "Montserrat", sans-serif;
    font-weight: 400;
    font-size: 17px;
    color: var(--red);
    letter-spacing: 1px;
    margin-top: 6px;
  }
  .contact__line {
    font-family: "Roboto", sans-serif;
    font-size: 17px;
    margin-top: 6px;
    display: flex;
    justify-content: flex-end;
    align-items: center;
    gap: 8px;
  }
  .contact__icon { width: 14px; height: 14px; }
  .brand {
    position: absolute;
    left: 62px;
    top: 172px;
    color: var(--red);
    font-family: "Montserrat", sans-serif;
  }
  .brand__name { font-weight: 800; font-size: 72px; line-height: 1; letter-spacing: 1px; }
  .brand__tagline {
    font-weight: 300;
    font-size: 27px;
    letter-spacing: 6px;
    margin-top: 8px;
    padding-left: 4px;
  }
  .motto--front { bottom: 17px; color: var(--black); }

  /* back */
  .back-brand {
    position: absolute;
    left: 60px;
    top: 196px;
    display: flex;
    align-items: center;
    gap: 14px;
  }
  .back-brand__dot { width: 40px; height: 40px; border-radius: 50%; background: var(--white); }
  .back-brand__name {
    font-family: "Montserrat", sans-serif;
    font-weight: 800;
    font-size: 28px;
    color: var(--white);
    letter-spacing: 1px;
  }
  .services {
    position: absolute;
    left: 60px;
    top: 254px;
    width: 670px;
    list-style: none;
    font-family: "Montserrat", sans-serif;
    font-weight: 500;
    font-size: 15px;
    line-height: 1.6;
    color: var(--white);
  }
  .services__item { display: flex; align-items: center; gap: 12px; }
  .services__item::before {
    content: "";
    width: 8px;
    height: 8px;
    flex: none;
    background: var(--red);
  }
  .motto--back { bottom: 30px; color: var(--red); }
</style>
</head>
<body>
<main class="canvas">

  <section class="card card--front" aria-label="Front of business card">
    <svg class="card__shapes" viewBox="0 0 780 450" aria-hidden="true">
      <rect class="band-white" x="0" y="355" width="780" height="30" fill="var(--white)"/>
      <rect class="band-red" x="0" y="385" width="780" height="65" fill="var(--red)"/>
    </svg>

    <div class="contact">
      <p class="contact__name">MARCO TELLIN</p>
      <p class="contact__role">PROPRIETOR</p>
      <p class="contact__line">
        <svg class="contact__icon" viewBox="0 0 24 24" aria-hidden="true"><path fill="var(--white)" d="M6.6 10.8a15.1 15.1 0 0 0 6.6 6.6l2.2-2.2c.3-.3.7-.4 1-.2 1.1.4 2.3.6 3.6.6.6 0 1 .4 1 1V20c0 .6-.4 1-1 1C10.6 21 3 13.4 3 4c0-.6.4-1 1-1h3.5c.6 0 1 .4 1 1 0 1.3.2 2.5.6 3.6.1.3 0 .7-.2 1z"/></svg>
        +503 - 418 - 6093
      </p>
      <p class="contact__line">@ hspumping@slabmail.example</p>
    </div>

    <div class="brand">
      <p class="brand__name">HARBORLINE</p>
      <p class="brand__tagline">SLAB PUMPING</p>
    </div>

    <p class="motto motto--front">JUST PUMP IT</p>
  </section>

  <section class="card card--back" aria-label="Back of business card">
    <svg class="card__shapes" viewBox="0 0 780 450" aria-hidden="true">
      <polygon class="chevron-red" points="96,0 780,0 780,125 96,45" fill="var(--red)"/>
      <path class="chevron-white" d="M62 -10 V78 L800 165" fill="none" stroke="var(--white)" stroke-width="24" stroke-linejoin="miter"/>
    </svg>

    <div class="back-brand">
      <span class="back-brand__dot"></span>
      <span class="back-brand__name">HARBORLINE</span>
    </div>

    <ul class="services">
      <li class="services__item">Years of experience in the world of concrete</li>
      <li class="services__item">Our pumps can do up to 70 yards an hour</li>
      <li class="services__item">Refer us to other contractors and get up to 10% off your next pump job</li>
      <li class="services__item">Call with any concrete related questions or to get a quote</li>
    </ul>

    <p class="motto motto--back">JUST PUMP IT</p>
  </section>

</main>
</body>
</html>
```